Redesign start page for existing online shop

We are selling building material (chimneys and flue pipes) as well as fireplaces (stoves). For this online shop we need a new start page. The domain is brunnfeld-bauwaren.de. Here you can see the current design. We want a smoother design with just one banner in the middle instead of the three in the first row. The look has to be more professional and trustworthy. You can therefore play with the colors. We want to try some different orange instead of our yellow / orange color. A few more things: - The phone number has to be bigger and more highlighted - So the 5 advantages at the top should be shown in a different way - New design for the products below - New footer

Target Market(s)

Germany and other countries in Europe.

Industry/Entity Type

Home Builder

Number of Pages Required

1 page

Other font styles liked:
• Please se the font on our current site.

Colors
f78f20
f68d4c

Requirements
Must have
• - Clear design - Trustworthy look - All elements Which are now shown shoulderstand be still there after redesigning -
Nice to have
• - See the Following sites to have a clou about our wishes: kalvesto.de flinkrabe.de

```html
<!DOCTYPE html>
<html lang="en">
<head>
<meta charset="utf-8">
<title>Brunnfeld Bauwaren – Start page</title>
<link href="https://fonts.googleapis.com/css2?family=Roboto:wght@300;400;500;700&display=swap" rel="stylesheet">
<style>
:root{
  --orange:#f78f20;
  --orange-2:#f68d4c;
  --ink:#3a3a3a;
  --muted:#8a8a8a;
  --line:#e6e8ec;
  --soft:#f6f8fb;
  --dark:#2f2f2f;
  --white:#ffffff;
  --stage:#e9eaec;
  --tip:#fbf3d9;
}
*{box-sizing:border-box;margin:0;padding:0}
html,body{width:672px;height:1200px;overflow:hidden;background:var(--stage);font-family:'Roboto',sans-serif;color:var(--ink)}
.viewport{position:absolute;left:143px;top:0;width:476px;height:1480px;transform:scale(.8108);transform-origin:0 0;background:var(--white);overflow:hidden}
.abs{position:absolute}
.tiny{font-size:4px;line-height:6px;color:var(--muted)}

/* top bar */
.topbar{left:0;top:0;width:476px;height:16px;background:var(--orange);color:var(--white);font-size:4px;font-weight:700;letter-spacing:.2px}
.topbar span{position:absolute;top:6px;white-space:nowrap}
.topbar .pill{position:absolute;left:180px;top:3px;width:148px;height:9px;border-radius:5px;background:var(--dark)}
.pill span{top:2.5px}

/* header */
.logo{display:flex;align-items:center;gap:4px}
.logo .dot{width:12px;height:12px;border-radius:50%;background:var(--orange)}
.logo b{font-size:7px;line-height:7px;font-weight:700;color:var(--ink);text-transform:uppercase;letter-spacing:.2px}
.search{left:150px;top:29px;width:140px;height:11px;border:1px solid var(--line);border-radius:6px;font-size:4px;color:var(--muted)}
.search span{white-space:nowrap}
.search .btn{position:absolute;right:-1px;top:-1px;width:34px;height:11px;border-radius:6px;background:var(--dark);color:var(--white);font-weight:700;text-align:center;line-height:11px}
.phone{left:310px;top:24px;display:flex;gap:4px;align-items:center}
.phone b{font-size:10px;font-weight:700;color:var(--ink);white-space:nowrap}
.phone small{display:block;font-size:3.5px;color:var(--muted);white-space:nowrap}
.cart{left:404px;top:16px;width:18px;height:20px;background:var(--orange);border-radius:0 0 9px 9px}

/* nav */
.nav{left:0;top:50px;width:476px;height:20px;border-top:1px solid var(--line);font-size:5px;font-weight:700}
.nav span{position:absolute;top:7px;white-space:nowrap}
.flag{display:inline-block;width:9px;height:6px;vertical-align:middle;background:linear-gradient(#111 33%,#d00 33% 66%,#fc0 66%)}

/* hero */
.hero{left:0;top:70px;width:476px;height:180px;background:linear-gradient(100deg,#d9d4cc 0%,#9db3cf 35%,#6a89b3 60%,#e9b733 85%,#cfa12a 100%)}
.benefits{left:56px;top:6px;display:flex;gap:12px;color:var(--white);font-size:4px;font-weight:700;white-space:nowrap}
.benefits i{display:inline-block;width:6px;height:6px;border-radius:50%;background:var(--orange);margin-right:3px;vertical-align:middle}
.badge{left:380px;top:0;width:42px;height:42px;border-radius:0 0 21px 21px;background:var(--white);text-align:center;font-size:4px;line-height:5px;font-weight:700;padding-top:24px}
.badge::before{content:"";position:absolute;left:15px;top:7px;width:12px;height:12px;border-radius:50%;background:#7a7a7a}
.hero h1{left:58px;top:52px;font-size:19px;font-weight:500;color:var(--white);white-space:nowrap}
.hero .sub{left:58px;top:80px;font-size:4px;font-weight:700;color:var(--white);line-height:6px}
.btn-o{background:var(--orange);color:var(--white);font-weight:700;text-align:center;border-radius:7px;white-space:nowrap}
.hero .cta{left:58px;top:98px;width:72px;height:12px;font-size:4.5px;line-height:12px}
.hero .price{left:64px;top:113px;font-size:10px;color:var(--white);white-space:nowrap}
.dots{left:58px;top:175px;display:flex;gap:3px}
.dots i{width:4px;height:4px;border-radius:50%;background:var(--white);opacity:.6}
.dots i:first-child{opacity:1}

/* brands */
.brands{left:0;top:250px;width:476px;height:42px;background:var(--soft)}
.brands .tag{left:56px;top:0;width:8px;height:30px;background:var(--orange);border-radius:0 0 4px 4px;color:var(--white);font-size:3.5px;line-height:8px;font-weight:700;writing-mode:vertical-rl;transform:rotate(180deg);text-align:center;white-space:nowrap}
.brands span{position:absolute;top:14px;font-size:10px;color:#777;font-weight:400;white-space:nowrap}

/* features */
.feature{width:176px;height:66px;border:1px solid var(--line);display:flex}
.feature .head{width:85px;border-right:1px solid var(--line);text-align:center;padding-top:10px;font-size:5px;font-weight:700;line-height:6px}
.feature .head svg{display:block;margin:0 auto 5px}
.feature p{flex:1;padding:12px 8px 0 10px;font-size:4px;line-height:6px;color:var(--muted)}

/* sections */
.band{left:0;width:476px;background:var(--soft)}
.title{left:0;width:476px;text-align:center;font-size:14px;font-weight:400;color:var(--ink)}
.subtitle{left:0;width:476px;text-align:center;font-size:4px;color:var(--muted)}
.step{width:54px;height:54px;border-radius:50%;background:var(--white);box-shadow:0 2px 6px rgba(0,0,0,.07);text-align:center;font-size:4px;font-weight:700;line-height:5px;padding-top:10px}
.step svg{display:block;margin:0 auto 4px}
.arrow{width:0;height:0;border-top:5px solid transparent;border-bottom:5px solid transparent;border-left:6px solid var(--white)}
.make{left:202px;width:72px;height:12px;font-size:4.5px;line-height:12px}

/* products */
.product{width:176px;height:66px;border:1px solid var(--line)}
.product .pic{position:absolute;left:0;top:0;width:86px;height:64px;border-right:1px solid var(--line)}
.product .pic div{position:absolute;left:18px;top:10px;width:48px;height:40px;border-radius:3px}
.product .from{position:absolute;left:57px;top:42px;width:28px;height:20px;background:var(--orange);color:var(--white);font-size:3.5px;text-align:center;line-height:5px;padding-top:3px;font-weight:700;white-space:nowrap}
.product .from b{font-size:5.5px}
.product h3{position:absolute;left:92px;top:6px;width:78px;text-align:center;font-size:5px;font-weight:700;line-height:6px}
.product p{position:absolute;left:94px;top:26px;width:74px;text-align:center;font-size:4px;line-height:6px;color:var(--muted)}
.product .go{position:absolute;right:-1px;bottom:-8px;width:8px;height:8px;background:var(--dark)}
.product .go::after{content:"";position:absolute;left:3px;top:2px;border-top:2px solid transparent;border-bottom:2px solid transparent;border-left:3px solid var(--white)}

/* why */
.why-text{left:213px;top:1102px;width:207px;height:208px;background:var(--white);border:1px solid var(--line)}
.why-text p{position:absolute;left:12px;width:184px;font-size:4px;line-height:6px;color:var(--muted)}
.tip{left:12px;top:80px;width:184px;height:38px;background:var(--tip);padding:5px 6px 0 20px;font-size:3.5px;line-height:5px;color:var(--muted)}
.tip b{color:var(--ink);display:block;font-size:4px}
.acc{left:0;width:205px;height:13px;border-top:1px solid var(--line);font-size:4px;font-weight:700;padding:4px 12px;white-space:nowrap}
.acc::after{content:"";position:absolute;right:10px;top:4px;width:3px;height:3px;border-right:1px solid var(--orange);border-bottom:1px solid var(--orange);transform:rotate(45deg)}

/* guarantee */
.guar h4{font-size:5px;font-weight:700}
.seal{border-radius:50%;background:radial-gradient(circle,#f5b400 0 45%,#2f2f2f 46% 100%)}
.made{width:72px;height:16px;background:var(--dark)}

/* footer */
.footer{left:0;top:1395px;width:476px;height:85px;border-top:1px solid var(--line)}
.footer h5{font-size:4px;font-weight:700}
.footer ul{list-style:none;font-size:3.5px;line-height:6px;color:var(--muted);white-space:nowrap}
.pay{font-size:4.5px;font-weight:700;color:#9a9a9a;white-space:nowrap}
</style>
</head>
<body>
<main class="viewport">

  <div class="abs topbar">
    <span style="left:58px">SICHER EINKAUFEN</span>
    <span style="left:102px">KONTAKT</span>
    <span style="left:128px">BERATUNG &amp; KONTAKT</span>
    <div class="pill">
      <span style="left:10px">IN 5 MIN DEAL</span>
      <span style="left:50px">LEADING BRANDS</span>
      <span style="left:90px">WITH US GET PROMOTION</span>
    </div>
    <span style="left:372px">SIGN UP</span>
    <span style="left:396px">MY ACCOUNT</span>
  </div>

  <div class="abs logo" style="left:56px;top:26px"><span class="dot"></span><b>Brunnfeld<br>Bauwaren</b></div>
  <div class="abs search"><span style="position:absolute;left:14px;top:3px">SEARCH</span><span style="position:absolute;left:66px;top:3px">SEARCH SITE</span><div class="btn">SEARCH</div></div>
  <div class="abs phone">
    <svg width="11" height="11" viewBox="0 0 24 24"><path fill="#f78f20" d="M6.6 10.8a15.1 15.1 0 0 0 6.6 6.6l2.2-2.2a1 1 0 0 1 1-.25 11.4 11.4 0 0 0 3.6.57 1 1 0 0 1 1 1V20a1 1 0 0 1-1 1A17 17 0 0 1 3 4a1 1 0 0 1 1-1h3.5a1 1 0 0 1 1 1c0 1.25.2 2.45.57 3.6a1 1 0 0 1-.25 1z"/></svg>
    <div><b>0800/555 0192</b><small>MON–FRI 8:00 – 18:00 HOTLINE</small></div>
  </div>
  <div class="abs cart"><svg style="margin:5px 4px" width="10" height="9" viewBox="0 0 24 22"><path fill="#fff" d="M2 2h4l3 12h11l3-9H8"/><circle cx="10" cy="19" r="2" fill="#fff"/><circle cx="19" cy="19" r="2" fill="#fff"/></svg></div>

  <nav class="abs nav">
    <span style="left:58px">ONLINE-SHOP ⌄</span>
    <span style="left:132px">SERVICE ⌄</span>
    <span style="left:200px">STANDORTE</span>
    <span style="left:266px">FUR HANDLER</span>
    <span style="left:336px">INSTALLATEURE</span>
    <span style="left:383px;top:5px"><i class="flag"></i> <b style="font-size:5px">GERMANY</b></span>
  </nav>

  <section class="abs hero" role="img" aria-label="Photo of an installer in a blue shirt and yellow hard hat marking a wall for a chimney">
    <div class="abs benefits">
      <span><i></i>GERMAN BRAND QUALITY</span>
      <span><i></i>25 YEAR WARRANTY</span>
      <span><i></i>FAST DELIVERY</span>
      <span><i></i>FREE CONSULTATION</span>
      <span><i></i>NATIONWIDE INSTALLATION SERVICE</span>
    </div>
    <div class="abs badge">★★★★★<br>VERY GOOD<br><span style="color:var(--muted)">4.71 / 5.00</span></div>
    <h1 class="abs">Mounting service</h1>
    <div class="abs sub">Nationwide steel chimney installation by professionals<br>at an unbeatable fixed price</div>
    <div class="abs btn-o cta">ADVANTAGE PRICE SAVE</div>
    <div class="abs price">from € 599,00</div>
    <div class="abs dots"><i></i><i></i><i></i></div>
  </section>

  <section class="abs brands">
    <div class="abs tag">OUR BRANDS</div>
    <span style="left:84px">norvald</span>
    <span style="left:180px">kestra</span>
    <span style="left:272px;font-size:7px;top:16px">HALD STEIN</span>
    <span style="left:358px;font-size:7px;top:16px">FLAMMWERK</span>
  </section>

  <div class="abs feature" style="left:56px;top:327px">
    <div class="head"><svg width="22" height="22" viewBox="0 0 24 24" fill="none" stroke="#f78f20" stroke-width="1.6"><path d="M3 11l9-8 9 8v10H3z"/><path d="M12 18c-2 0-3-1.5-2-3.5 1 1 1.5-1 2-2.5 1 1.5 3 3 2 4.5-.4 1-1 1.5-2 1.5z"/></svg>Mandatory heating<br>supply immediately!</div>
    <p>Enter a few key data to your house in our offer computer and get a few hours a binding offer for your new heating !</p>
  </div>
  <div class="abs feature" style="left:243px;top:327px">
    <div class="head"><svg width="22" height="22" viewBox="0 0 24 24" fill="none" stroke="#f78f20" stroke-width="1.6"><circle cx="12" cy="9" r="6"/><circle cx="12" cy="9" r="3"/><path d="M8 14l-2 8 6-3 6 3-2-8"/></svg>More than 30 years<br>master quality!</div>
    <p>Experience and competence are the guarantee of an excellent service. With around 150 trained and competent heating professionals we are in Germany working for you!</p>
  </div>
  <div class="abs feature" style="left:56px;top:405px">
    <div class="head"><svg width="22" height="22" viewBox="0 0 24 24" fill="none" stroke="#f78f20" stroke-width="1.6"><rect x="3" y="9" width="18" height="12"/><path d="M2 9h20M12 9v12M12 9c-3-5-7-3-4 0M12 9c3-5 7-3 4 0"/></svg>New heating already<br>from 39 € per month!</div>
    <p>A new environmentally friendly and energy saving heating supply and we install already for 39,- Euro per month. The possible energy savings your new heating system is almost "gift"!</p>
  </div>
  <div class="abs feature" style="left:243px;top:405px">
    <div class="head"><svg width="22" height="22" viewBox="0 0 24 24" fill="none" stroke="#f78f20" stroke-width="1.6"><rect x="6" y="2" width="12" height="20" rx="2"/><path d="M10 18h4M9 10l2 2 4-4"/></svg>10 year warranty on<br>your new heater!</div>
    <p>Enter a few key data to your house in our offer computer and get a few hours a binding offer for your new heating !</p>
  </div>

  <section class="abs band" style="top:505px;height:232px"></section>
  <h2 class="abs title" style="top:530px">How it works</h2>
  <div class="abs subtitle" style="top:550px">In a few steps to the right offer for Their renovation</div>
  <div class="abs step" style="left:98px;top:588px"><svg width="12" height="12" viewBox="0 0 24 24" fill="none" stroke="#f78f20" stroke-width="2"><rect x="5" y="3" width="14" height="18"/><path d="M8 8h8M8 12h8M8 16h5"/></svg>Enter data<br>online</div>
  <div class="abs arrow" style="left:153px;top:610px"></div>
  <div class="abs step" style="left:170px;top:588px"><svg width="12" height="12" viewBox="0 0 24 24" fill="none" stroke="#f78f20" stroke-width="2"><circle cx="12" cy="8" r="4"/><path d="M4 21c1-5 15-5 16 0"/></svg>aufma und<br>beratung durch<br>kundenberater</div>
  <div class="abs arrow" style="left:225px;top:610px"></div>
  <div class="abs step" style="left:242px;top:588px"><svg width="12" height="12" viewBox="0 0 24 24" fill="none" stroke="#f78f20" stroke-width="2"><circle cx="10" cy="8" r="4"/><path d="M3 21c1-5 13-5 14 0M16 12l2 2 4-4"/></svg>angebot von 3<br>energiefeld</div>
  <div class="abs arrow" style="left:297px;top:610px"></div>
  <div class="abs step" style="left:314px;top:588px;padding-top:16px"><svg width="14" height="12" viewBox="0 0 26 20" fill="none" stroke="#f78f20" stroke-width="2"><rect x="1" y="3" width="15" height="11"/><path d="M16 7h5l4 4v3h-9"/><circle cx="6" cy="16" r="2"/><circle cx="20" cy="16" r="2"/></svg>execution</div>
  <div class="abs arrow" style="left:369px;top:610px"></div>
  <div class="abs subtitle" style="top:666px">Now suggested a request ask!</div>
  <div class="abs btn-o make" style="top:691px">MAKE INQUIRY</div>

  <h2 class="abs title" style="top:762px">Our Products</h2>
  <div class="abs product" style="left:56px;top:805px">
    <div class="pic" role="img" aria-label="Product photo of a metal chimney cover"><div style="background:linear-gradient(135deg,#ececec,#9a9a9a)"></div></div>
    <div class="from">FROM<br><b>€ 116,50</b></div>
    <h3>chimney cover</h3>
    <p>Fireplace covers for all chimneys purchased individually. Highest durability and quality for your chimney.</p>
    <div class="go"></div>
  </div>
  <div class="abs product" style="left:245px;top:805px">
    <div class="pic" role="img" aria-label="Product photo of a wall duct fitting"><div style="background:linear-gradient(135deg,#f1efe9,#b9b4a8)"></div></div>
    <div class="from">FROM<br><b>€ 99,90</b></div>
    <h3>Wanddurchführung</h3>
    <p>Wanddurchführungen für die sichere Durchführung von Abgasrohren durch Hauswände. Brandschutz auf höchstem Niveau.</p>
    <div class="go"></div>
  </div>
  <div class="abs product" style="left:56px;top:884px">
    <div class="pic" role="img" aria-label="Product photo of a black wood-burning stove"><div style="left:30px;width:24px;background:linear-gradient(#333,#111)"></div></div>
    <div class="from">FROM<br><b>€1.159,00</b></div>
    <h3>Kaminofen</h3>
    <p>Kaminöfen mit hervorragendem Preis / Leistungsverhältnis versandkostenfrei online bestellen. Langlebige Qualität und Sicherheit für Ihr Haus.</p>
    <div class="go"></div>
  </div>
  <div class="abs product" style="left:245px;top:884px">
    <div class="pic" role="img" aria-label="Product photo of a lightweight chimney kit with red cap"><div style="left:28px;width:28px;background:linear-gradient(#a33,#999 40%,#ccc)"></div></div>
    <div class="from">FROM<br><b>€ 63,00</b></div>
    <h3>Lightweight<br>construction chimney</h3>
    <p>Lightweight construction chimneys are the perfect solution for an interior chimney. Light elements allow for quick and easy installation.</p>
    <div class="go"></div>
  </div>
  <div class="abs btn-o make" style="top:974px">MORE PRODUCTS</div>

  <section class="abs band" style="top:1010px;height:310px"></section>
  <h2 class="abs title" style="top:1032px">Why we are best</h2>
  <div class="abs subtitle" style="top:1056px;font-size:6px;line-height:9px;color:var(--ink)">Stainless steel chimneys, chimney extensions, stovepipes and<br>chimney accessories - at brunnfeld-bauwaren.de buy anything</div>
  <div class="abs" style="left:56px;top:1102px;width:138px;height:138px;background:linear-gradient(140deg,#7e8a95,#b9a276 55%,#6d6e70)" role="img" aria-label="Photo of a roofer using a nail gun on roof shingles"></div>
  <div class="abs why-text">
    <p style="top:10px">Can I use a steel chimney for sale on the Internet? This question you have probably never asked. For other products which is a matter of course, but with a stainless steel chimney you do not think first to the online shopping . There are the all around the subject for several years various platforms steel chimney offer.</p>
    <p style="top:46px">However, these providers operate their web shop only incidentally. This is reflected in the poor usability and the partly very outdated technology of pages. Brunnfeld Bauwaren has gone a new way here.</p>
    <div class="abs tip"><svg style="position:absolute;left:6px;top:6px" width="9" height="11" viewBox="0 0 18 22" fill="none" stroke="#f78f20" stroke-width="1.6"><path d="M9 2a6 6 0 0 0-3 11v3h6v-3A6 6 0 0 0 9 2zM6 19h6"/></svg><b>Another tip:</b>All chimneys can be wonderfully with a stovepipe connect, devices. Here there is a large breadth of various lengths, colors and angles. In addition, more recently insulated stovepipes are available. This double-walled pipe reduces the distance to combustible materials to a minimum.</div>
    <div class="abs acc" style="top:128px">Steel chimney, chimney kit and stainless steel chimney - all from one source.</div>
    <div class="abs acc" style="top:141px">old chimney extension and cowl extension low self..</div>
    <div class="abs acc" style="top:154px">Chimney cap, chimney cover and Kaminabdeckplatte stainless steel to measure.</div>
    <div class="abs acc" style="top:167px">Chimney fans, draft stabilizer, fire doors and other specialty products</div>
  </div>

  <div class="abs seal" style="left:58px;top:1333px;width:38px;height:38px"></div>
  <div class="abs guar" style="left:110px;top:1336px;width:100px">
    <h4>25-year guarantee</h4>
    <div class="tiny" style="margin-top:4px">To meet our premium quality and our service pledges, please contact us, of course, 25 year guarantee on all stainless steel chimneys and steel chimney components.</div>
  </div>
  <div class="abs made" style="left:232px;top:1345px"></div>
  <div class="abs tiny" style="left:328px;top:1336px;width:92px">We offer exclusive products of German brand manufacturers. Our full range is manufactured from industry leaders and is subject to constant quality controls. For your safety only the best for a fair price.</div>

  <footer class="abs footer">
    <div class="abs logo" style="left:56px;top:18px"><span class="dot"></span><b>Brunnfeld<br>Bauwaren</b></div>
    <div class="abs tiny" style="left:56px;top:40px;width:80px">© 2016 BRUNNFELD BAUWAREN.DE<br>ALL RIGHTS RESERVED</div>
    <div class="abs" style="left:150px;top:20px"><h5>OTHER LINKS</h5>
      <ul style="margin-top:4px"><li>FREQUENTLY ASKED QUESTIONS</li><li>ABOUT US</li><li>CONDITIONS</li><li>RETURNS/DELIVERY</li><li>DATA PROTECTION</li></ul></div>
    <div class="abs" style="left:228px;top:28px"><ul><li>IMPRINT</li><li>CONTACT US</li><li>BLOG</li><li>GLOSSARY</li></ul></div>
    <div class="abs" style="left:328px;top:20px;width:100px"><h5>WE ACCEPT</h5>
      <div style="display:flex;gap:8px;margin-top:8px" class="pay"><span>Velquin</span><span>Tandor</span><span>Nolvex</span><span>Brisko</span></div>
      <div style="display:flex;gap:10px;margin-top:6px;font-size:3.5px" class="pay"><span>Kaufpass</span><span>Vorab</span><span>Rechnung</span></div>
    </div>
  </footer>

</main>
</body>
</html>
```